New business card with our logo

we finalized our logo with the help of pixel harbor - now we need a business card using that logo. we are a metal service center providing raw steel and metal products for fabricating, contractors, artists, etc. we have the wording for the back of the card figured out (attached, no deviations from text please), just need help putting it all together.
would like the look of steel somehow incorporated in the design ... would like the black part of the logo to be steel or silver color (the S & BRANLEY)
Other font styles liked:
- calibri, arial, similar to those, modern looking
Colors
Designer to choose colors to be used in the design.
Requirements
Must have
- Back of card must haves are attached (no deviations from wording please).
- FRONT of card:
- logo
- address
- name
- office tel
- cell
- fax
- website
- address
Nice to have
- incorporate the look of steel or element of steel somehow
- names of the staff on front not in all caps, i.e. Rosvita not ROSVITA
- this industry is more industrial, not coffee or flower shop so design should be aligned with that
- design should be classic and tasteful

```html
<!DOCTYPE html>
<html lang="en">
<head>
<meta charset="utf-8">
<title>Branley Steel – Business Card</title>
<link href="https://fonts.googleapis.com/css2?family=Arimo:ital,wght@0,400;0,700;1,700&display=swap" rel="stylesheet">
<style>
  :root {
    --steel-light: #8d9396;
    --steel-mid: #6a7073;
    --steel-dark: #464b4d;
    --brushed-top: #4b5253;
    --brushed-mid: #2d3233;
    --brushed-bottom: #1b1e1f;
    --silver: #e4e7e9;
    --white: #ffffff;
  }
  * { margin: 0; padding: 0; box-sizing: border-box; }
  html, body { width: 927px; height: 1200px; overflow: hidden; background: #ffffff; }
  body { font-family: "Arimo", Arial, sans-serif; color: var(--white); }

  .card-sheet { position: relative; width: 927px; height: 1200px; }
  .card-face { position: absolute; left: 0; width: 927px; height: 600px; overflow: hidden; }

  /* Back of card: promotional side */
  .card-back {
    top: 0;
    background:
      radial-gradient(ellipse at 30% 20%, rgba(255,255,255,0.18), transparent 60%),
      radial-gradient(ellipse at 80% 85%, rgba(0,0,0,0.25), transparent 60%),
      repeating-linear-gradient(115deg, rgba(255,255,255,0.05) 0 1px, transparent 1px 9px),
      linear-gradient(160deg, var(--steel-light), var(--steel-mid) 45%, var(--steel-dark));
  }
  .brand-name {
    position: absolute; top: 105px; width: 100%; text-align: center;
    font-size: 70px; font-weight: 700; line-height: 76px;
    color: var(--silver); letter-spacing: 1px; white-space: nowrap;
  }
  .service-title {
    position: absolute; top: 244px; width: 100%; text-align: center;
    font-size: 45px; font-weight: 700; letter-spacing: 0.5px;
    text-shadow: 0 2px 4px rgba(0,0,0,0.5);
  }
  .service-list {
    position: absolute; top: 293px; width: 100%; text-align: center;
    font-size: 29px; font-weight: 400; letter-spacing: 0.5px;
    text-shadow: 0 2px 3px rgba(0,0,0,0.4);
  }
  .divider {
    position: absolute; top: 353px; left: 132px; width: 664px; height: 2px;
    background: var(--white);
  }
  .product-list {
    position: absolute; top: 381px; width: 100%; text-align: center;
    font-size: 25px; font-weight: 700; line-height: 34px;
    text-shadow: 0 2px 3px rgba(0,0,0,0.5);
  }
  .product-list .dot { font-size: 13px; padding: 0 10px; vertical-align: middle; }
  .product-list .dot-wide { padding: 0 36px; }
  .tagline {
    position: absolute; top: 480px; width: 100%; text-align: center;
    font-size: 31px; font-weight: 700; font-style: italic;
    text-shadow: 0 2px 4px rgba(0,0,0,0.55);
  }

  /* Front of card: contact side */
  .card-front {
    top: 600px;
    background:
      radial-gradient(ellipse at 50% 15%, rgba(255,255,255,0.12), transparent 55%),
      repeating-linear-gradient(0deg, rgba(255,255,255,0.03) 0 1px, transparent 1px 3px),
      linear-gradient(180deg, var(--brushed-top), var(--brushed-mid) 50%, var(--brushed-bottom));
  }
  .front-brand {
    position: absolute; top: 134px; width: 100%; text-align: center;
    font-size: 48px; font-weight: 700; line-height: 56px;
    color: var(--white); letter-spacing: 1px;
  }
  .staff-name {
    position: absolute; top: 309px; left: 132px;
    font-size: 35px; font-weight: 700; font-style: italic;
  }
  .contact-column {
    position: absolute; top: 382px;
    font-size: 30px; font-weight: 700; font-style: italic; line-height: 39px;
    list-style: none;
  }
  .contact-left { left: 132px; }
  .contact-right { right: 132px; text-align: right; }
</style>
</head>
<body>
<main class="card-sheet">
  <section class="card-face card-back">
    <div class="brand-name">BRANLEY STEEL</div>
    <h1 class="service-title">METAL SERVICE CENTER</h1>
    <p class="service-list">CUT • SHEAR &nbsp;• &nbsp;PUNCH • LIGHT FAB</p>
    <div class="divider"></div>
    <p class="product-list">
      Structural Steel<span class="dot dot-wide">●</span>Stainless &amp; Aluminum<br>
      Building Components<span class="dot">●</span>Rebar<span class="dot">●</span>Decking<span class="dot">●</span>...and more!
    </p>
    <p class="tagline">Cut to size, Pick-up or Delivered!</p>
  </section>

  <section class="card-face card-front">
    <div class="front-brand">BRANLEY STEEL</div>
    <p class="staff-name">John Doe</p>
    <ul class="contact-column contact-left">
      <li>adress.......</li>
      <li>email@email.com</li>
      <li>www.webadress.com</li>
    </ul>
    <ul class="contact-column contact-right">
      <li>off: 555-555</li>
      <li>mob: 000-000</li>
      <li>fax: 000-000</li>
    </ul>
  </section>
</main>
</body>
</html>
```